Toravel Project Consulting

I need a logo and business card design for a small business operating in the management consulting and contractor space, predominantly in local and state government. I specialise in project management, financial consulting, people and culture, procurement, ICT transformation and contracting for corporate support areas of organisations.

Industry/Entity Type

Business

```html
<!DOCTYPE html>
<html lang="en">
<head>
<meta charset="utf-8">
<title>Toravel Project Consulting – Business Card</title>
<link rel="stylesheet" href="https://fonts.googleapis.com/css2?family=Lato:ital,wght@0,400;0,700;1,400&display=swap">
<style>
  :root {
    --page: #ffffff;
    --card-blue: #0b3f96;
    --card-blue-deep: #072f78;
    --card-blue-bright: #1456c0;
    --panel-top: #02060f;
    --text-white: #ffffff;
    --brand-light: #e8f1ff;
    --mark-blue: #5fb6ea;
    --sky: #9fd0ea;
    --city: #5a6a7a;
  }
  * { margin: 0; padding: 0; box-sizing: border-box; }
  html, body { width: 1031px; height: 1200px; overflow: hidden; background: var(--page); }
  body { position: relative; font-family: "Lato", sans-serif; color: var(--text-white); }

  .card { position: absolute; left: 53px; width: 879px; height: 514px; overflow: hidden; }
  .card--front { top: 52px; background: var(--card-blue); }
  .card--back {
    top: 589px;
    background: linear-gradient(180deg, #0a2f78 0%, #1250b8 32%, #0b3f96 55%, #0c44a0 100%);
  }

  .holder-name { position: absolute; left: 83px; top: 52px; font-size: 39px; font-weight: 700; letter-spacing: 0.5px; }
  .holder-role { position: absolute; left: 83px; top: 112px; font-size: 32px; font-style: italic; }
  .contact { position: absolute; left: 83px; display: flex; align-items: center; gap: 18px; font-size: 34px; }
  .contact svg { width: 30px; height: 30px; }
  .contact--phone { top: 240px; }
  .contact--email { top: 295px; }
  .address { position: absolute; left: 80px; top: 412px; font-size: 33px; }

  .scene-photo { position: absolute; top: 0; height: 173px; }
  .scene-photo--left {
    left: 0; width: 203px;
    background: linear-gradient(180deg, var(--sky) 0%, #6f8ea6 40%, #8a4a3c 65%, #1a4f9a 100%);
  }
  .scene-photo--right {
    right: 0; width: 203px;
    background: linear-gradient(180deg, var(--sky) 0%, #c3d4df 35%, var(--city) 62%, #1a4f9a 100%);
  }
  .services-panel {
    position: absolute; left: 203px; top: 0; width: 473px; height: 383px;
    background: linear-gradient(180deg, var(--panel-top) 0%, #0a1f4a 30%, #1252bb 75%, rgba(11,63,150,0) 100%);
  }
  .services {
    position: absolute; left: 231px; top: 62px; list-style: none;
    font-size: 28px; line-height: 40.5px; letter-spacing: 0.3px;
  }
  .services li { position: relative; padding-left: 48px; }
  .services li::before {
    content: ""; position: absolute; left: 0; top: 14px; width: 11px; height: 11px;
    background: var(--text-white); transform: rotate(45deg);
  }
  .services li.continued::before { display: none; }

  .brand { position: absolute; left: 60px; top: 352px; display: flex; align-items: center; gap: 36px; }
  .brand-dot { width: 110px; height: 110px; border-radius: 50%; background: var(--mark-blue); }
  .brand-name { font-size: 36px; font-weight: 700; letter-spacing: 2px; text-transform: uppercase; color: var(--brand-light); }
</style>
</head>
<body>
  <section class="card card--front" aria-label="Business card front">
    <h1 class="holder-name">DANIEL HARTLEY</h1>
    <p class="holder-role">Director</p>
    <p class="contact contact--phone">
      <svg viewBox="0 0 24 24" aria-hidden="true"><rect x="6" y="2" width="12" height="20" rx="2" fill="none" stroke="#fff" stroke-width="2.4"/><rect x="8" y="5" width="8" height="10" fill="#fff"/></svg>
      <span>9123 45678</span>
    </p>
    <p class="contact contact--email">
      <svg viewBox="0 0 24 24" aria-hidden="true"><rect x="2" y="5" width="20" height="14" fill="none" stroke="#fff" stroke-width="2.2"/><path d="M2 5 L12 13 L22 5" fill="none" stroke="#fff" stroke-width="2.2"/></svg>
      <span>hello@toravel.example</span>
    </p>
    <p class="address">12 Marlow Parade, Kelsbury NSW 2064</p>
  </section>

  <section class="card card--back" aria-label="Business card back">
    <div class="scene-photo scene-photo--left" role="img" aria-label="City skyline with a red desert rock reflected in water"></div>
    <div class="scene-photo scene-photo--right" role="img" aria-label="Harbour city skyline with opera house"></div>
    <div class="services-panel"></div>
    <ul class="services">
      <li>PROJECT MANAGEMENT</li>
      <li>FINANCIAL CONSULTING</li>
      <li>PEOPLE AND CULTURE</li>
      <li>PROCUREMENT</li>
      <li>ICT TRANSFORMATION</li>
      <li>CORPORATE SUPPORT</li>
      <li class="continued">AREAS OF ORGANISATIONS</li>
    </ul>
    <div class="brand">
      <span class="brand-dot" aria-hidden="true"></span>
      <span class="brand-name">Toravel Project Consulting</span>
    </div>
  </section>
</body>
</html>
```